Attractive Flyer for Moving Company

Our Company called "Harborlight Moving Company".
We provide moving service for home and businesses
We need a flyer for a moving company, located in San Diego, CA USA
Flyer size will be 7 x 5 inches, double sided.

Flyer needs to be very attractive and catchy for eye. I want people to keep it even if they dont need our service. I attached a lot of text in separate word file.
Logo, brief and additional pictures are attached.

Target Market(s)

27 years - 55 Years old

Industry/Entity Type

Moving Company

Colors
ec1f27
3176b5
ffffff

Requirements
Must have
• Attached in Word File
Nice to have
• Please be creative in placing a text and selecting a back ground picture.

```html
<!DOCTYPE html>
<html lang="en">
<head>
<meta charset="utf-8">
<title>Harborlight Moving Company – Flyer</title>
<link rel="stylesheet" href="https://fonts.googleapis.com/css2?family=Exo+2:wght@600;700&family=Lato:ital,wght@0,400;1,700&family=Oswald:wght@500;700&display=swap">
<style>
  :root {
    --red: #d71a22;
    --navy: #102f86;
    --navy-dark: #0b246b;
    --white: #ffffff;
    --ink: #1b1b1b;
    --gray-band: #e6e6e8;
    --divider: #e2e2e2;
    --page: #ffffff;
  }
  * { margin: 0; padding: 0; box-sizing: border-box; }
  html, body { width: 1029px; height: 1200px; overflow: hidden; background: var(--page); }

  .flyer {
    position: absolute; left: 142px; top: 75px;
    width: 739px; height: 1036px;
    background: var(--white);
    overflow: hidden;
  }

  .hero-photo {
    position: absolute; left: 0; top: 0; width: 739px; height: 352px;
    background: linear-gradient(135deg, #efe6da 0%, #d9b88f 40%, #8fa7cf 62%, #e7cfb3 100%);
  }

  .brand-panel {
    position: absolute; left: 0; top: 100px; width: 235px; height: 129px;
    background: rgba(255,255,255,0.72);
    display: flex; flex-direction: column; justify-content: center; padding-left: 18px;
  }
  .brand-name {
    font-family: "Exo 2", sans-serif; font-weight: 700; color: var(--red);
    line-height: 1.05;
  }
  .brand-name .lead { display: block; font-size: 33px; letter-spacing: -0.5px; }
  .brand-name .tail { display: block; font-size: 17px; padding-left: 30px; }

  .headline-band {
    position: absolute; left: 0; top: 352px; width: 739px; height: 121px;
    background: var(--navy);
  }
  .headline {
    position: absolute; left: 21px; top: 5px;
    font-family: "Oswald", sans-serif; font-weight: 700; color: var(--red);
    font-size: 57px; line-height: 70px; letter-spacing: 0.3px;
  }
  .subheadline {
    position: absolute; left: 21px; top: 71px;
    font-family: "Oswald", sans-serif; font-weight: 500; color: var(--white);
    font-size: 33px; line-height: 40px; transform: scaleX(0.86); transform-origin: left;
  }

  .badge { position: absolute; left: 518px; top: 297px; width: 206px; height: 206px; }
  .badge-text {
    position: absolute; left: 518px; top: 297px; width: 206px; height: 206px;
    display: flex; flex-direction: column; align-items: center; justify-content: center;
    color: var(--white); text-align: center;
  }
  .badge-text .need { font-family: "Exo 2", sans-serif; font-weight: 700; font-size: 40px; line-height: 42px; }
  .badge-text .movers { font-family: "Oswald", sans-serif; font-weight: 500; font-size: 50px; line-height: 54px; margin-bottom: 12px; }

  .section-title {
    position: absolute; top: 492px;
    font-family: "Exo 2", sans-serif; font-weight: 700; color: var(--red); font-size: 29px;
  }
  .why-title { left: 27px; }
  .services-title { left: 434px; top: 496px; }

  .column-divider {
    position: absolute; left: 400px; top: 529px; width: 1px; height: 309px; background: var(--divider);
  }

  .bullet-list { position: absolute; list-style: none; font-family: "Lato", sans-serif; color: var(--ink); }
  .bullet-list li { position: relative; padding-left: 19px; font-size: 19.5px; line-height: 25px; margin-bottom: 10px; }
  .bullet-list li::before {
    content: ""; position: absolute; left: 0; top: 10px; width: 6px; height: 6px; border-radius: 50%; background: var(--red);
  }
  .why-list { left: 30px; top: 557px; font-style: italic; font-weight: 700; letter-spacing: -0.3px; }
  .services-list { left: 438px; top: 566px; }
  .services-list li { font-size: 20px; }

  .estimate-band {
    position: absolute; left: 0; top: 857px; width: 739px; height: 115px; background: var(--gray-band);
  }
  .call-for {
    position: absolute; left: 27px; top: 22px;
    font-family: "Exo 2", sans-serif; font-weight: 700; color: var(--red); font-size: 39px; line-height: 40px;
  }
  .quick-estimate {
    position: absolute; left: 29px; top: 66px;
    font-family: "Oswald", sans-serif; font-weight: 500; color: var(--navy); font-size: 33px; line-height: 40px;
    transform: scaleX(0.9); transform-origin: left;
  }
  .contact { position: absolute; left: 377px; top: 30px; width: 340px; }
  .phone-line { font-family: "Lato", sans-serif; font-weight: 700; font-size: 27px; color: var(--navy); line-height: 34px; white-space: nowrap; }
  .phone-line .number { color: var(--ink); font-style: normal; }
  .online-line {
    font-family: "Oswald", sans-serif; font-weight: 500; font-size: 23px; color: var(--red); line-height: 30px;
    transform: scaleX(0.88); transform-origin: left; white-space: nowrap;
  }

  .footer-band {
    position: absolute; left: 0; top: 994px; width: 739px; height: 42px; background: var(--navy);
    display: flex; align-items: center; justify-content: center;
  }
  .web-address {
    font-family: "Lato", sans-serif; font-size: 19px; color: var(--white); letter-spacing: 7px;
  }
</style>
</head>
<body>
  <main class="flyer">
    <div class="hero-photo" role="img" aria-label="Photo of a smiling family sitting among cardboard moving boxes, with a teddy bear and a laptop"></div>

    <div class="brand-panel">
      <p class="brand-name"><span class="lead">HARBORLIGHT</span><span class="tail">Moving Company</span></p>
    </div>

    <section class="headline-band">
      <h1 class="headline">QUALITY FOCUSED</h1>
      <p class="subheadline">CUSTOMER RECOMMENDED MOVERS</p>
    </section>

    <svg class="badge" viewBox="0 0 206 206" aria-hidden="true">
      <circle cx="103" cy="103" r="102" fill="var(--white)"/>
      <circle cx="103" cy="103" r="96" fill="var(--navy-dark)"/>
      <circle cx="103" cy="103" r="91" fill="var(--white)"/>
      <circle cx="103" cy="103" r="88" fill="var(--red)"/>
    </svg>
    <div class="badge-text">
      <span class="need">Need</span>
      <span class="movers">MOVERS</span>
    </div>

    <h2 class="section-title why-title">Why Call Us?</h2>
    <ul class="bullet-list why-list">
      <li>Customer Oriented Service</li>
      <li>Years of Great reputation</li>
      <li>Affordable pricing</li>
      <li>Professional, efficient, strong movers</li>
      <li>We always handle your<br>belongings with care</li>
      <li>Clean and equipped trucks</li>
      <li>Absolutely NO surprising fees</li>
    </ul>

    <div class="column-divider"></div>

    <h2 class="section-title services-title">Moving Services</h2>
    <ul class="bullet-list services-list">
      <li>Residential</li>
      <li>Long Distance</li>
      <li>Commercial</li>
      <li>Loading / Unloading rental<br>truck / portable storage</li>
      <li>Packing Service</li>
    </ul>

    <section class="estimate-band">
      <p class="call-for">CALL FOR</p>
      <p class="quick-estimate">A QUICK ESTIMATE</p>
      <div class="contact">
        <p class="phone-line">Toll Free: <span class="number">1-855-555-0142</span></p>
        <p class="online-line">Or Request Your Estimate online</p>
      </div>
    </section>

    <footer class="footer-band">
      <span class="web-address">www.HarborlightMoving.com</span>
    </footer>
  </main>
</body>
</html>
```